Harmony Swift Care Business card

We want a business card that matches our business theme. Our website is www.swiftcarehub.example
The company name is Harmony Swift Care
The persons having the business cards will be doctors
My logo is attached.
We have a drive-thru medical center where our motto is Fast, Reliable, and Convenient. Our goal is to change the medical space while utilizing technologies, keeping a professional and clean look

Medical

Info on the card should be: Name, Position, Cell number, website, email address, possibly the office line as well

Requirements
Must have
• Logo
Nice to have
• Professional medical feel with our logo colors incorporated

```html
<!DOCTYPE html>
<html lang="en">
<head>
<meta charset="utf-8">
<title>Harmony Swift Care – Business Card</title>
<link href="https://fonts.googleapis.com/css2?family=Roboto:wght@300;400;500;700&display=swap" rel="stylesheet">
<style>
  :root {
    --brand-blue: #1c4aa3;
    --accent-cyan: #3fbdea;
    --ink: #1d1d22;
    --muted: #6b6b72;
    --paper: #ffffff;
    --stage: #e4e6ea;
  }
  * { box-sizing: border-box; margin: 0; padding: 0; }
  html, body { width: 1200px; height: 780px; overflow: hidden; }
  body {
    background: var(--stage);
    font-family: "Roboto", Arial, sans-serif;
    display: flex;
    align-items: center;
    justify-content: center;
    gap: 40px;
  }
  .card {
    position: relative;
    width: 540px;
    height: 310px;
    background: var(--paper);
    border-radius: 16px;
    overflow: hidden;
    box-shadow: 0 6px 18px rgba(0,0,0,.12);
  }
  .card__band {
    position: absolute;
    left: 0; right: 0; bottom: 0;
    height: 62px;
    background: var(--brand-blue);
    border-top: 4px solid var(--accent-cyan);
    box-shadow: 0 -5px 0 var(--paper);
  }
  .brand {
    position: absolute;
    color: var(--brand-blue);
    font-weight: 700;
    white-space: nowrap;
  }
  .card--front .brand {
    top: 40px; left: 40px;
    font-size: 20px;
  }
  .card--back .brand {
    top: 104px; left: 0; right: 0;
    text-align: center;
    font-size: 34px;
  }

  .person {
    position: absolute;
    top: 86px; left: 296px;
  }
  .person__name {
    font-size: 22px;
    font-weight: 500;
    color: var(--ink);
  }
  .person__role {
    font-size: 12px;
    font-weight: 300;
    color: var(--muted);
    margin-top: 2px;
  }
  .person__rule {
    width: 34px; height: 2px;
    background: var(--brand-blue);
    margin-top: 5px;
  }
  .contact {
    position: absolute;
    top: 146px; left: 230px;
    display: flex;
    gap: 12px;
  }
  .contact__icons {
    width: 22px;
    height: 54px;
    background: var(--brand-blue);
    border-radius: 6px;
    display: flex;
    flex-direction: column;
    align-items: center;
    justify-content: space-around;
    padding: 3px 0;
  }
  .contact__icons svg { width: 11px; height: 11px; }
  .contact__lines {
    font-size: 11.5px;
    font-weight: 400;
    color: var(--ink);
    line-height: 17px;
  }
  .contact__lines .contact__address { color: var(--muted); }
</style>
</head>
<body>

  <section class="card card--front">
    <p class="brand">Harmony Swift Care</p>

    <div class="person">
      <p class="person__name">Daniel Reyes</p>
      <p class="person__role">CEO &amp; Founder</p>
      <div class="person__rule"></div>
    </div>

    <div class="contact">
      <div class="contact__icons">
        <svg viewBox="0 0 24 24" aria-label="phone"><path fill="#fff" d="M6.6 10.8a15 15 0 0 0 6.6 6.6l2.2-2.2c.3-.3.7-.4 1-.2 1.1.4 2.3.6 3.6.6.6 0 1 .4 1 1V20c0 .6-.4 1-1 1A17 17 0 0 1 3 4c0-.6.4-1 1-1h3.5c.6 0 1 .4 1 1 0 1.3.2 2.5.6 3.6.1.3 0 .7-.2 1z"/></svg>
        <svg viewBox="0 0 24 24" aria-label="email"><path fill="#fff" d="M3 5h18v14H3zm2 2v.5l7 4.5 7-4.5V7l-7 4.5z"/></svg>
        <svg viewBox="0 0 24 24" aria-label="website"><circle cx="12" cy="12" r="9" fill="none" stroke="#fff" stroke-width="2"/><path d="M3 12h18M12 3c3 3 3 15 0 18M12 3c-3 3-3 15 0 18" fill="none" stroke="#fff" stroke-width="1.6"/></svg>
      </div>
      <div class="contact__lines">
        <p>+1 555 014 2287</p>
        <p>hello@swiftcarehub.example</p>
        <p>www.swiftcarehub.example</p>
        <p class="contact__address">48 Meadow Lane, Suite 2</p>
        <p class="contact__address">Brookfield, zip code - 10452</p>
      </div>
    </div>

    <div class="card__band"></div>
  </section>

  <section class="card card--back">
    <p class="brand">Harmony Swift Care</p>
    <div class="card__band"></div>
  </section>

</body>
</html>
```